Infographic for B2B Service solution offering (sales funnel)

Attached is an example of something we need assistance with making into a more professional infographic. These infographics are for our B2B marketing services, aimed at IT Consulting firms.

We have done some basic graphics (attached) and this will provide you guidance (video link on google sheet):
https://pages.vardolink.net/sheet/r/7kQm3TzP9wLcYe2HbNvAsDxR4uFgJ8tWoZiE6yKpBq/view?mode=shared

Here are some examples you can model for the new infographic:
https://vault.vardolink.net/store/groups/48PkTwMz3nRq9LbXvYc-hsd2FjQe?ref=store_link

Target Market(s)

B2B IT Consulting Firms

Industry/Entity Type

Information Technology, Consulting

Colors

Designer to choose colors to be used in the design.

Requirements
Must have
• professional, high level consulting firms are target market
Should not have
• cartoonish

```html
<!DOCTYPE html>
<html lang="en">
<head>
<meta charset="utf-8">
<title>Creating B2B Relationship – Trust Building Offers Method</title>
<link rel="stylesheet" href="https://fonts.googleapis.com/css2?family=Montserrat:wght@400;500;700;800&family=Oswald:wght@500;600&display=swap">
<style>
  :root {
    --bg: #ebeeed;
    --navy: #0e4673;
    --navy-deep: #0b3c66;
    --rule: #1a4f7c;
    --leader: #8a8f93;
    --low: #d7261e;
    --high: #2a8a2a;
    --gold: #f2b11e;
    --teal: #26b49b;
    --blue: #2a7fc4;
    --orange: #e5603b;
    --plum: #584a6c;
    --crimson: #c02f4d;
    --rust: #a5421d;
    --white: #ffffff;
  }
  * { margin: 0; padding: 0; box-sizing: border-box; }
  html, body { width: 1200px; height: 1200px; overflow: hidden; background: var(--bg); }
  .canvas { position: relative; width: 1200px; height: 1200px; background: var(--bg); overflow: hidden; }
  .headline {
    position: absolute; left: 0; right: 0; top: 62px;
    text-align: center; color: var(--navy);
    font-family: "Montserrat", sans-serif; font-weight: 800;
    font-size: 38px; line-height: 66px; letter-spacing: 0.5px;
  }
  .divider { position: absolute; left: 138px; width: 924px; top: 213px; height: 3px; background: var(--rule); }
  .subhead {
    position: absolute; left: 0; right: 0; top: 258px; text-align: center;
    color: var(--navy); font-family: "Montserrat", sans-serif; font-weight: 800; font-size: 35px;
  }
  .entry-label {
    position: absolute; left: 0; right: 0; top: 338px; text-align: center;
    color: var(--navy); font-family: "Montserrat", sans-serif; font-weight: 500; font-size: 36px;
  }
  .funnel-art { position: absolute; left: 0; top: 0; width: 1200px; height: 1200px; }
  .footer-band { position: absolute; left: 0; right: 0; bottom: 0; height: 30px; background: var(--navy-deep); }
  .tier-title { font-family: "Oswald", sans-serif; font-weight: 500; fill: var(--white); font-size: 16px; }
  .tier-offer { font-family: "Montserrat", sans-serif; font-weight: 700; fill: var(--white); font-size: 6.6px; }
  .trust-label { font-family: "Montserrat", sans-serif; font-weight: 800; font-size: 9.5px; }
</style>
</head>
<body>
<main class="canvas">
  <h1 class="headline">CREATING B2B REALATIONSHIP<br>THE BUILD UP “TRUST BUILDING OFFERS” METHOD</h1>
  <div class="divider"></div>
  <h2 class="subhead">HOW RELATIONSHIP ARE BUILT</h2>
  <p class="entry-label">COLD LEADS</p>

  <svg class="funnel-art" viewBox="0 0 800 800" xmlns="http://www.w3.org/2000/svg">
    <defs>
      <linearGradient id="tier-shade" x1="0" x2="1" y1="0" y2="0">
        <stop offset="0" stop-color="#000" stop-opacity="0.28"/>
        <stop offset="0.4" stop-color="#fff" stop-opacity="0.12"/>
        <stop offset="0.6" stop-color="#fff" stop-opacity="0.05"/>
        <stop offset="1" stop-color="#000" stop-opacity="0.32"/>
      </linearGradient>
      <linearGradient id="rim-water" x1="0" x2="0" y1="0" y2="1">
        <stop offset="0" stop-color="#1f7fc4"/>
        <stop offset="1" stop-color="#7ccdf2"/>
      </linearGradient>
      <linearGradient id="trust-scale" gradientUnits="userSpaceOnUse" x1="0" y1="335" x2="0" y2="745">
        <stop offset="0" stop-color="#d7261e"/>
        <stop offset="0.35" stop-color="#ef8a2a"/>
        <stop offset="0.55" stop-color="#e6d72a"/>
        <stop offset="0.75" stop-color="#6fbf3a"/>
        <stop offset="1" stop-color="#1f8a2a"/>
      </linearGradient>

      <path id="tier-wife" d="M345,712 A35,9 0 0 1 415,712 L407,760 A27,7 0 0 1 353,760 Z"/>
      <path id="tier-move" d="M316,650 A64,11 0 0 1 444,650 L425,712 A45,9 0 0 1 335,712 Z"/>
      <path id="tier-meet" d="M296,585 A84,12 0 0 1 464,585 L444,650 A64,11 0 0 1 316,650 Z"/>
      <path id="tier-weekend" d="M275,520 A105,12 0 0 1 485,520 L464,585 A84,12 0 0 1 296,585 Z"/>
      <path id="tier-dinner" d="M255,455 A125,13 0 0 1 505,455 L485,520 A105,12 0 0 1 275,520 Z"/>
      <path id="tier-coffee" d="M235,388 A145,13 0 0 1 525,388 L505,455 A125,13 0 0 1 255,455 Z"/>
      <path id="tier-phone" d="M215,325 A165,14 0 0 1 545,325 L525,388 A145,13 0 0 1 235,388 Z"/>
    </defs>

    <!-- entry arrow -->
    <g class="entry-arrow" fill="var(--navy)">
      <rect x="375" y="262" width="10" height="26"/>
      <path d="M363,285 L397,285 L380,310 Z"/>
    </g>

    <!-- trust scale -->
    <g class="trust-scale">
      <line x1="160" y1="335" x2="160" y2="745" stroke="url(#trust-scale)" stroke-width="3" stroke-dasharray="4 4"/>
      <path d="M147,741 L160,754 L173,741" fill="none" stroke="#1f8a2a" stroke-width="3"/>
      <text class="trust-label" x="116" y="374" fill="var(--low)">LOW</text>
      <text class="trust-label" x="108" y="390" fill="var(--low)">TRUST</text>
      <text class="trust-label" x="102" y="694" fill="var(--high)">HIGH</text>
      <text class="trust-label" x="102" y="710" fill="var(--high)">TRUST</text>
    </g>

    <!-- funnel tiers, bottom first so upper tiers overlap -->
    <g class="funnel">
      <use href="#tier-wife" fill="var(--rust)"/><use href="#tier-wife" fill="url(#tier-shade)"/>
      <use href="#tier-move" fill="var(--crimson)"/><use href="#tier-move" fill="url(#tier-shade)"/>
      <use href="#tier-meet" fill="var(--plum)"/><use href="#tier-meet" fill="url(#tier-shade)"/>
      <use href="#tier-weekend" fill="var(--orange)"/><use href="#tier-weekend" fill="url(#tier-shade)"/>
      <use href="#tier-dinner" fill="var(--blue)"/><use href="#tier-dinner" fill="url(#tier-shade)"/>
      <use href="#tier-coffee" fill="var(--teal)"/><use href="#tier-coffee" fill="url(#tier-shade)"/>
      <use href="#tier-phone" fill="var(--gold)"/><use href="#tier-phone" fill="url(#tier-shade)"/>
      <ellipse cx="380" cy="325" rx="165" ry="14" fill="#e2a21a"/>
      <ellipse cx="380" cy="326" rx="159" ry="11" fill="url(#rim-water)"/>
    </g>

    <!-- tier labels -->
    <g class="tier-labels" text-anchor="middle">
      <text class="tier-title" x="380" y="362">PHONE#</text>
      <text class="tier-offer" x="380" y="378">Offer #1 : LOW RISK,  LOW INVESTMENT</text>

      <text class="tier-title" x="380" y="429">COFEE</text>
      <text class="tier-offer" x="380" y="445">Offer #2 : LOW RISK,  MEDIUM INVESTMENT</text>

      <text class="tier-title" x="380" y="492">DINNER</text>
      <text class="tier-offer" x="380" y="508">Offer #3 : MEDIUM RISK,  MEDIUM INVESTMENT</text>

      <text class="tier-title" x="380" y="555">WEEKEND TRAVEL</text>
      <text class="tier-offer" x="380" y="567">Offer #4 : HIGH RISK,</text>
      <text class="tier-offer" x="380" y="576">MEDIUM INVESTMENT</text>

      <text class="tier-title" x="380" y="617">MEET PARTNERS</text>
      <text class="tier-offer" x="380" y="632">Offer #5 : MEDIUM RISK,</text>
      <text class="tier-offer" x="380" y="641">HIGH INVESTMENT</text>

      <text class="tier-title" x="380" y="680" style="font-size:15px">MOVE IN</text>
      <text class="tier-offer" x="380" y="694">Offer #6 : HIGH RISK,</text>
      <text class="tier-offer" x="380" y="703">HIGH INVESTMENT</text>

      <text class="tier-title" x="380" y="734" style="font-size:12px">WIFE</text>
      <text class="tier-offer" x="380" y="744" style="font-size:4.2px">Offer #7 : HIGH RISK,</text>
      <text class="tier-offer" x="380" y="750" style="font-size:4.2px">HIGH INVESTMENT</text>
    </g>

    <!-- leader lines -->
    <g class="leaders" stroke="var(--leader)" stroke-width="1">
      <line x1="570" y1="369" x2="602" y2="369"/>
      <line x1="541" y1="431" x2="602" y2="431"/>
      <line x1="509" y1="492" x2="605" y2="492"/>
      <line x1="484" y1="558" x2="605" y2="558"/>
      <line x1="455" y1="623" x2="607" y2="623"/>
      <line x1="432" y1="683" x2="605" y2="683"/>
      <line x1="412" y1="739" x2="605" y2="739"/>
    </g>

    <!-- icons -->
    <g class="icons">
      <g class="icon-phone" fill="var(--gold)">
        <path d="M632,352 q-8,4 -4,18 q6,18 20,24 q8,3 12,-4 l-7,-7 q-3,4 -7,2 q-8,-6 -11,-16 q0,-4 4,-5 z"/>
        <path d="M648,356 a10,10 0 0 1 8,8" fill="none" stroke="var(--gold)" stroke-width="2"/>
        <path d="M648,350 a16,16 0 0 1 14,14" fill="none" stroke="var(--gold)" stroke-width="2"/>
      </g>
      <g class="icon-coffee" fill="none" stroke="var(--teal)" stroke-width="2.5">
        <path d="M628,426 h30 v6 a15,12 0 0 1 -30,0 z" fill="var(--teal)" stroke="none"/>
        <path d="M658,429 a5,5 0 0 1 0,10"/>
        <path d="M624,446 h40"/>
        <path d="M638,420 q-3,-4 0,-8 M644,420 q-3,-4 0,-8 M650,420 q-3,-4 0,-8" stroke-width="1.5"/>
      </g>
      <g class="icon-dinner" fill="var(--blue)">
        <rect x="625" y="485" width="3" height="28" rx="1"/>
        <circle cx="645" cy="499" r="12"/>
        <rect x="662" y="485" width="3" height="28" rx="1"/>
      </g>
      <g class="icon-suitcase" fill="var(--orange)">
        <rect x="621" y="543" width="46" height="33" rx="2"/>
        <path d="M636,543 v-6 h16 v6" fill="none" stroke="var(--orange)" stroke-width="3"/>
        <rect x="629" y="543" width="2.5" height="33" fill="var(--bg)"/>
        <rect x="657" y="543" width="2.5" height="33" fill="var(--bg)"/>
      </g>
      <g class="icon-handshake">
        <path d="M614,618 l14,-6 l12,8 l-6,10 z" fill="var(--plum)"/>
        <path d="M668,618 l-14,-6 l-16,10 l10,12 z" fill="#2f4f7a"/>
        <path d="M636,622 l8,8 l6,-2 l-6,-8 z" fill="#e7c3a0"/>
      </g>
      <g class="icon-luggage" fill="var(--crimson)">
        <rect x="628" y="673" width="34" height="24" rx="3"/>
        <path d="M638,673 v-5 h14 v5" fill="none" stroke="var(--crimson)" stroke-width="2.5"/>
        <rect x="644" y="673" width="2" height="24" fill="var(--bg)"/>
      </g>
      <rect class="icon-couple" x="624" y="724" width="34" height="30" rx="6" fill="var(--rust)" role="img" aria-label="Couple icon"/>
    </g>
  </svg>

  <div class="footer-band"></div>
</main>
</body>
</html>
```